Quorvex clinic business card - double sided for young clinic

I require business cards for my aesthetic clinic specialising in the below treatments. I would like the cards to be modern as my clinic base are young 22-35 years old. I require my logo on it and would like the edges to be rounded.

I have an aesthetic clinic specialising in :
Quorvex
Lip Enhancement
Chemical Peels
Facial Fillers
Non Surgical Face Lift

I would the cards to have the following information on them:
My logo - (in grey/silver)
address
Phone number
services

Colours :
White/grey/silver and red

a nice image on there, perhaps a set of lips as this is a main service i deliver

Company Name: PDA Address: 52 Farrowmere Road, 4 Brackwell High Street, KT9 4WQ Phone: 0208 794 2160 Website: www.penningtondoweaesthetics.co.uk

Target Market(s)

clinics 22-45 years old mainly female

Industry/Entity Type

Business

Contact Information for Business Card

as above

Requirements
Must have
• logo
• Address
• Email
• Phone number
• Services i offer
Nice to have
• images

```html
<!DOCTYPE html>
<html lang="en">
<head>
<meta charset="utf-8">
<title>PDA – Business Card</title>
<link rel="stylesheet" href="https://fonts.googleapis.com/css2?family=Tinos&family=Open+Sans:wght@400&family=Questrial&display=swap">
<style>
  :root {
    --backdrop: #dcdcdc;
    --card-white: #ffffff;
    --card-black: #000000;
    --brand-red: #c8161d;
    --heading-red: #d2262e;
    --ink: #1a1a1a;
    --mark-dark: #231f20;
    --silver: #a9a9a9;
    --list-white: #ffffff;
  }
  * { box-sizing: border-box; margin: 0; padding: 0; }
  html, body { width: 1189px; height: 1200px; overflow: hidden; }
  body { background: var(--backdrop); position: relative; }

  .card {
    position: absolute;
    left: 140px;
    width: 917px;
    height: 524px;
    border-radius: 49px;
    overflow: hidden;
  }
  .card--front { top: 45px; background: var(--card-white); }
  .card--back { top: 624px; background: var(--card-black); }

  /* Front */
  .brand-panel {
    position: absolute;
    left: 46px; top: 47px;
    width: 419px; height: 437px;
    border-radius: 41px;
    background: var(--brand-red);
    display: flex; flex-direction: column;
    align-items: center; justify-content: center;
    gap: 26px;
  }
  .brand-name {
    font-family: "Tinos", serif;
    color: var(--mark-dark);
    text-align: center;
    letter-spacing: 0.14em;
    text-transform: uppercase;
    line-height: 1.1;
  }
  .brand-name__short { display: block; font-size: 50px; letter-spacing: 0.08em; }
  .brand-name__full { display: block; font-size: 28px; margin-top: 22px; }

  .person { position: absolute; left: 515px; top: 110px; font-family: "Tinos", serif; }
  .person__name { font-size: 31px; color: var(--brand-red); line-height: 1.1; }
  .person__role { font-size: 23px; color: var(--ink); line-height: 1.2; }

  .contact-list {
    position: absolute; left: 515px; top: 357px;
    list-style: none;
    font-family: "Tinos", serif;
    font-size: 19.5px; color: var(--ink); line-height: 23px;
  }
  .contact-list li { display: flex; gap: 13px; align-items: flex-start; }
  .contact-list li + li { margin-top: 1px; }
  .contact-icon { flex: none; width: 16px; height: 16px; margin-top: 3px; }

  /* Back */
  .services { position: absolute; left: 62px; top: 56px; }
  .services__title {
    font-family: "Open Sans", sans-serif;
    font-weight: 400;
    font-size: 52px;
    color: var(--heading-red);
    line-height: 1.2;
    margin-bottom: 14px;
  }
  .services__list {
    list-style: none;
    font-family: "Questrial", sans-serif;
    font-size: 24.5px;
    color: var(--list-white);
  }
  .services__list li { display: flex; align-items: center; gap: 18px; height: 37px; }
  .services__bullet { width: 24px; height: 24px; flex: none; }

  .back-brand {
    position: absolute;
    left: 484px; top: 212px;
    width: 384px; height: 257px;
    display: flex; flex-direction: column;
    align-items: center; justify-content: center;
  }
  .back-brand .brand-name { color: var(--silver); }
  .back-brand .brand-name__short { font-size: 58px; }
  .back-brand .brand-name__full { font-size: 30px; margin-top: 30px; }
</style>
</head>
<body>

<section class="card card--front" aria-label="Card front">
  <div class="brand-panel">
    <p class="brand-name">
      <span class="brand-name__short">PDA</span>
      <span class="brand-name__full">Pennington Dowe<br>Aesthetics</span>
    </p>
  </div>

  <div class="person">
    <p class="person__name">Owen Halbrook</p>
    <p class="person__role">Manager</p>
  </div>

  <ul class="contact-list">
    <li>
      <svg class="contact-icon" viewBox="0 0 16 16" aria-hidden="true">
        <rect width="16" height="16" fill="#c8161d"/>
        <path d="M5 3.5 L7 3.5 L7.6 6 L6.4 7 C7 8.4 7.8 9.3 9.2 9.8 L10.2 8.6 L12.6 9.2 L12.6 11.2 C12.6 11.8 12 12.4 11.2 12.3 C7.4 11.8 4.3 8.7 3.8 5 C3.7 4.2 4.3 3.5 5 3.5 Z" fill="#fff"/>
      </svg>
      <span>0208 794 2160</span>
    </li>
    <li>
      <svg class="contact-icon" viewBox="0 0 16 16" aria-hidden="true">
        <rect width="16" height="16" fill="#c8161d"/>
        <circle cx="8" cy="8" r="5" fill="none" stroke="#fff" stroke-width="1.3"/>
        <ellipse cx="8" cy="8" rx="2.1" ry="5" fill="none" stroke="#fff" stroke-width="1"/>
        <line x1="3" y1="8" x2="13" y2="8" stroke="#fff" stroke-width="1"/>
      </svg>
      <span>www.penningtondoweaesthetics.co.uk</span>
    </li>
    <li>
      <svg class="contact-icon" viewBox="0 0 16 16" aria-hidden="true">
        <rect width="16" height="16" fill="#c8161d"/>
        <path d="M8 2.8 C5.9 2.8 4.4 4.4 4.4 6.3 C4.4 8.8 8 13 8 13 C8 13 11.6 8.8 11.6 6.3 C11.6 4.4 10.1 2.8 8 2.8 Z" fill="#fff"/>
        <circle cx="8" cy="6.3" r="1.4" fill="#c8161d"/>
      </svg>
      <span>52 Farrowmere Road, 4 Brackwell High<br>Street, KT9 4WQ</span>
    </li>
  </ul>
</section>

<section class="card card--back" aria-label="Card back">
  <div class="services">
    <h2 class="services__title">Service :</h2>
    <ul class="services__list">
      <li><svg class="services__bullet" viewBox="0 0 24 24" aria-hidden="true"><g stroke="#d2262e" stroke-width="2.4" stroke-linecap="round"><line x1="12" y1="2" x2="12" y2="22"/><line x1="3.3" y1="7" x2="20.7" y2="17"/><line x1="3.3" y1="17" x2="20.7" y2="7"/></g></svg>Quorvex</li>
      <li><svg class="services__bullet" viewBox="0 0 24 24" aria-hidden="true"><g stroke="#d2262e" stroke-width="2.4" stroke-linecap="round"><line x1="12" y1="2" x2="12" y2="22"/><line x1="3.3" y1="7" x2="20.7" y2="17"/><line x1="3.3" y1="17" x2="20.7" y2="7"/></g></svg>Lip Enhancement</li>
      <li><svg class="services__bullet" viewBox="0 0 24 24" aria-hidden="true"><g stroke="#d2262e" stroke-width="2.4" stroke-linecap="round"><line x1="12" y1="2" x2="12" y2="22"/><line x1="3.3" y1="7" x2="20.7" y2="17"/><line x1="3.3" y1="17" x2="20.7" y2="7"/></g></svg>Chemical Peels</li>
      <li><svg class="services__bullet" viewBox="0 0 24 24" aria-hidden="true"><g stroke="#d2262e" stroke-width="2.4" stroke-linecap="round"><line x1="12" y1="2" x2="12" y2="22"/><line x1="3.3" y1="7" x2="20.7" y2="17"/><line x1="3.3" y1="17" x2="20.7" y2="7"/></g></svg>Facial Fillers</li>
      <li><svg class="services__bullet" viewBox="0 0 24 24" aria-hidden="true"><g stroke="#d2262e" stroke-width="2.4" stroke-linecap="round"><line x1="12" y1="2" x2="12" y2="22"/><line x1="3.3" y1="7" x2="20.7" y2="17"/><line x1="3.3" y1="17" x2="20.7" y2="7"/></g></svg>Non Surgical Face Lift</li>
    </ul>
  </div>

  <div class="back-brand">
    <p class="brand-name">
      <span class="brand-name__short">PDA</span>
      <span class="brand-name__full">Pennington Dowe<br>Aesthetics</span>
    </p>
  </div>
</section>

</body>
</html>
```